A resume/portfolio website for myself

I'm an independent software contractor, architect, tech trainer. I need a web site to present myself. Many ready to use portfolio designs are too artistic and focused on presenting design skills of the person. I like a nice website but the content should be a little less graphic than if you would present a graphic designer. Content could be presentation of me, core skill qualities and services and resume. Potentially a page with my tech courses in the longer run

```html
<!DOCTYPE html>
<html lang="en">
<head>
<meta charset="utf-8">
<title>Daniel Varga — Software Contractor &amp; Trainer</title>
<link href="https://fonts.googleapis.com/css2?family=Montserrat:wght@500;700&display=swap" rel="stylesheet">
<style>
  :root {
    --ink: #111111;
    --paper: #ffffff;
    --accent: #ffff00;
    --glow: #fdfba8;
    --shirt: #9fb6cc;
    --skin: #b98768;
  }
  html, body {
    margin: 0;
    padding: 0;
    overflow: hidden;
    background: var(--paper);
  }
  .page {
    position: relative;
    width: 1200px;
    height: 675px;
    overflow: hidden;
    background: var(--paper);
    font-family: "Montserrat", Arial, sans-serif;
    color: var(--ink);
  }
  .brand {
    position: absolute;
    left: 76px;
    top: 50px;
    display: flex;
    align-items: center;
    gap: 8px;
    font-weight: 700;
    font-size: 34px;
    line-height: 40px;
    color: var(--ink);
  }
  .brand-square {
    width: 12px;
    height: 12px;
    background: var(--ink);
  }
  .main-nav a {
    position: absolute;
    top: 50px;
    font-weight: 500;
    font-size: 18.5px;
    color: var(--ink);
    text-decoration: none;
  }
  .nav-home { left: 611px; }
  .nav-about { left: 732px; }
  .nav-contact { left: 853px; }
  .nav-skills { left: 988px; top: 49px !important; }

  .hero-title {
    position: absolute;
    left: 70px;
    top: 209px;
    margin: 0;
    font-weight: 700;
    font-size: 58px;
    line-height: 66px;
    letter-spacing: 0.5px;
  }
  .hero-intro {
    position: absolute;
    left: 77px;
    top: 344px;
    width: 540px;
    margin: 0;
    font-weight: 500;
    font-size: 16.5px;
    line-height: 31.6px;
  }
  .cta {
    position: absolute;
    left: 77px;
    top: 485px;
    width: 230px;
    height: 52px;
    box-sizing: border-box;
    border: 3.5px solid var(--ink);
    border-radius: 7px;
    display: flex;
    align-items: center;
    padding-left: 25px;
    gap: 22px;
    font-weight: 500;
    font-size: 21px;
    color: var(--ink);
    text-decoration: none;
  }
  .cta svg { width: 14px; height: 22px; }

  .glow {
    position: absolute;
    left: 600px;
    top: 300px;
    width: 700px;
    height: 500px;
    background: radial-gradient(ellipse at 55% 70%, var(--glow) 0%, rgba(253,251,168,0.5) 35%, rgba(255,255,255,0) 65%);
  }
  .portrait-frame {
    position: absolute;
    left: 646px;
    top: 133px;
    width: 384px;
    height: 504px;
    box-sizing: border-box;
    border: 17.5px solid var(--accent);
  }
  .portrait {
    position: absolute;
    left: 722px;
    top: 172px;
    width: 362px;
    height: 503px;
    border-radius: 150px 150px 0 0;
    background: linear-gradient(180deg, var(--skin) 0%, var(--skin) 30%, var(--shirt) 42%, #b3c6d8 100%);
  }
  .slide-dots {
    position: absolute;
    left: 1119px;
    top: 263px;
    display: flex;
    flex-direction: column;
    gap: 43px;
  }
  .slide-dots span {
    width: 22px;
    height: 22px;
    border-radius: 50%;
    background: var(--ink);
  }
</style>
</head>
<body>
<div class="page">
  <div class="brand"><span class="brand-square"></span>DV</div>

  <nav class="main-nav">
    <a class="nav-home" href="#">Home</a>
    <a class="nav-about" href="#">About</a>
    <a class="nav-contact" href="#">Contact</a>
    <a class="nav-skills" href="#">Skills</a>
  </nav>

  <h1 class="hero-title">Hi, I am<br>Daniel Varga</h1>
  <p class="hero-intro">I am an independent software contractor and architect. I design systems that scale and I train teams to build and run them with confidence.</p>

  <a class="cta" href="#">KNOW MORE
    <svg viewBox="0 0 14 22" aria-hidden="true"><polyline points="3,2 11,11 3,20" fill="none" stroke="#111111" stroke-width="3" stroke-linecap="round" stroke-linejoin="round"/></svg>
  </a>

  <div class="glow"></div>
  <div class="portrait-frame"></div>
  <div class="portrait" role="img" aria-label="Portrait photo of the site owner in a light blue shirt, arms crossed"></div>

  <div class="slide-dots"><span></span><span></span><span></span></div>
</div>
</body>
</html>
```